The Willowmere Clinic Flyer Design

The Willowmere Clinic is a new company providing Dietetic services for people with gastrointestinal disorders. The main client base would be people suffering from Irritable Bowel Syndrome. IBS is a collection of symptoms which (will be individual to the suffer) including constipation/diarrhoea/abdominal pain or discomfort/bloating/belching/flatulence/stomach gurgling/reflux/nausea/urgency/incomplete emptying/fatigue/headaches. IBS affects approx 30% of the population. Previous treatments have generally been ineffectual and include medication, hypnotherapy, healthy eating.
Recently it has been found that the FODMAP diet (a diet low in fermentable Carbohydrates) has been effective in 75% of sufferers.
The Low FODMAP diet is complex and it is highly recommended that it is undertaken only under the supervision of a suitably qualified dietitian. Treatment is available within the QRV but is usually accessible only following consultation with a Gastroenterologist. Most GP's have never heard of this treatment as the research was only published in 2009 in Australia and is yet to filter through to the general practitioner. The Willowmere Clinic is the only clinic in the UK offering dietetic lead specialist services.
I am a member of the ZLO and MVRT (logos provided)
The flyer would be double sided, informing the patient of all the self help steps they could take if they have IBS then recommending that they contact The Willowmere Clinic for specialist advice.
Self Help: Healthy eating, regular meals, good intake of non caffeinated non alcoholic non fizzy drinks, regular exercise, stress management.
The flyer would be left in GP surgeries, Health centres, holistic therapy centres, or through doors.
Target Market(s)
Majority female aged 20-50, able to pay for private services
Industry/Entity Type
Clinic
Look and feel
Each slider illustrates characteristics of the customer's brand and the style your logo design should communicate.

```html
<!DOCTYPE html>
<html lang="en">
<head>
<meta charset="utf-8">
<title>The Willowmere Clinic – Flyer Front</title>
<link rel="stylesheet" href="https://fonts.googleapis.com/css2?family=Lobster&family=Open+Sans:wght@400;700&family=Arvo:ital,wght@1,400;1,700&display=swap">
<style>
  :root {
    --stage: #2a2a2a;
    --sky: #19a9d9;
    --paper: #f3f3f3;
    --ink: #1c1c1c;
    --white: #ffffff;
    --bullet: #f7b461;
    --ribbon: #fbb96a;
    --ribbon-end: #e3a25a;
    --ribbon-text: #17687f;
    --badge-diet: #1ba0d8;
    --badge-reg: #27467f;
  }
  html, body {
    margin: 0;
    width: 1200px;
    height: 839px;
    overflow: hidden;
    background: var(--stage);
  }
  .flyer {
    position: absolute;
    left: 105px;
    top: 65px;
    width: 932px;
    height: 660px;
    background: var(--paper);
    overflow: hidden;
    font-family: "Open Sans", Arial, sans-serif;
  }
  .sky-panel {
    position: absolute;
    left: 0; top: 0;
    width: 932px; height: 490px;
    background: var(--sky);
  }
  .hero-photo {
    position: absolute;
    left: 0; top: 0;
    width: 405px; height: 660px;
    background: linear-gradient(180deg, #cfc6b4 0%, #bdb29c 45%, #b79a83 60%, #bfb5a0 75%, #6f93bd 88%, #5b82b0 100%);
  }
  .decor {
    position: absolute;
    left: 0; top: 0;
  }
  .brand {
    position: absolute;
    left: 505px; top: 32px;
    display: flex;
    align-items: center;
    gap: 22px;
    color: var(--ink);
  }
  .brand-mark {
    width: 62px; height: 62px;
    border-radius: 50%;
    background: var(--ink);
  }
  .brand-name {
    font-weight: 400;
    line-height: 1;
  }
  .brand-name .line-1 { display: block; font-size: 33px; }
  .brand-name .line-2 { display: block; font-size: 44px; margin-top: 2px; }
  .headline {
    position: absolute;
    left: 360px; top: 140px;
    width: 540px;
    margin: 0;
    text-align: center;
    font-family: "Lobster", cursive;
    font-weight: 400;
    font-size: 48px;
    color: var(--white);
  }
  .symptoms {
    position: absolute;
    left: 398px; top: 232px;
    margin: 0; padding: 0;
    list-style: none;
    display: grid;
    grid-template-columns: 172px 180px;
    grid-auto-flow: column;
    grid-template-rows: repeat(5, 37.5px);
    color: var(--white);
    font-weight: 700;
    font-size: 17px;
  }
  .symptoms li {
    position: relative;
    padding-left: 21px;
  }
  .symptoms li::before {
    content: "";
    position: absolute;
    left: 0; top: 9px;
    width: 9px; height: 9px;
    border-radius: 50%;
    background: var(--bullet);
  }
  .question {
    position: absolute;
    left: 812px; top: 240px;
    font-weight: 700;
    font-size: 118px;
    line-height: 1;
    color: var(--white);
  }
  .ribbon-text {
    position: absolute;
    left: 405px; top: 456px;
    width: 410px;
    text-align: center;
    font-family: "Arvo", Georgia, serif;
    font-style: italic;
    color: var(--ribbon-text);
    line-height: 1.2;
  }
  .ribbon-text .lead { display: block; font-weight: 700; font-size: 23px; }
  .ribbon-text .follow { display: block; font-weight: 400; font-size: 18px; }
  .badge {
    position: absolute;
  }
  .badge-dietitians {
    left: 410px; top: 562px;
    width: 180px; height: 50px;
    background: var(--badge-diet);
    border-radius: 4px;
  }
  .badge-registered {
    left: 662px; top: 552px;
    width: 80px; height: 82px;
    background: var(--badge-reg);
  }
</style>
</head>
<body>
  <main class="flyer">
    <div class="sky-panel"></div>
    <div class="hero-photo" role="img" aria-label="Photo of a person in a beige sweater and jeans holding their stomach in discomfort"></div>

    <svg class="decor" width="932" height="660" viewBox="0 0 932 660" aria-hidden="true">
      <path class="symptom-frame" d="M386 222 H773 V303 L800 320 L773 337 V422 H386 Z"
            fill="none" stroke="#ffffff" stroke-width="1.5" stroke-dasharray="6 5" stroke-linejoin="round"/>
      <polygon class="ribbon-end" points="360,452 412,452 412,525 360,525 380,488" fill="var(--ribbon-end)"/>
      <polygon class="ribbon-end" points="808,452 860,452 840,488 860,525 808,525" fill="var(--ribbon-end)"/>
      <rect class="ribbon-band" x="405" y="452" width="410" height="70" fill="var(--ribbon)"/>
    </svg>

    <div class="brand">
      <span class="brand-mark"></span>
      <span class="brand-name"><span class="line-1">The Willowmere</span><span class="line-2">Clinic</span></span>
    </div>

    <h1 class="headline">What’s your gut feeling?</h1>

    <ul class="symptoms">
      <li>nausea</li>
      <li>constipation</li>
      <li>diarrhoea</li>
      <li>abdominal pain</li>
      <li>vomiting</li>
      <li>tired all the time</li>
      <li>headaches</li>
      <li>low mood</li>
      <li>indigestion</li>
      <li>reflux</li>
    </ul>

    <div class="question">?</div>

    <p class="ribbon-text">
      <span class="lead">Don’t worry we have the</span>
      <span class="follow">new solution for that symptoms!</span>
    </p>

    <div class="badge badge-dietitians" role="img" aria-label="ZLO membership badge"></div>
    <div class="badge badge-registered" role="img" aria-label="MVRT registration badge"></div>
  </main>
</body>
</html>
```